General Contractors need a new Crisp updated Card Design

We need a new business card design for our company of 25 years based in Toronto call Holvaster Building Inc. : Our goal is to be the leading commercial contractors in Toronto by providing exceptional value to our clients. We work very hard to deliver professional, quality, service in conjunction with consistent price competitiveness to all of our clients on every single project.

Target Market(s)

Design & Build Clients

Industry/Entity Type

Construction Company

Contact Information for Business Card

Address:
18 North Tamlin Glen Road, Unit 57, Marbrook Vale, ON, K7T 2R9
Office: 905-218-5937

Holvasters Logo
Employee Job Description
Employee Cell Phone #
Employee Email
www.holvaster-example.com

Colors

Designer to choose colors to be used in the design.

Requirements
Must have
• Quote Company Saying:
• "Professional. Quality. Service."
Nice to have
• New Crisp up to date look. simple & fresh ( Not to Busy)
Should not have
• NO BLUE PRINTS ON THE BUSINESS CARDS

```html
<!DOCTYPE html>
<html lang="en">
<head>
<meta charset="utf-8">
<title>Holvaster Building Inc. – Business Card</title>
<link rel="stylesheet" href="https://fonts.googleapis.com/css2?family=Roboto:wght@400;500;700&display=swap">
<style>
  :root {
    --teal: #00705f;
    --teal-light: #acc6bb;
    --card-white: #ffffff;
    --text-grey: #4f4f4f;
    --backdrop: #e8e5e0;
    --shadow: rgba(0, 0, 0, 0.28);
  }
  * { margin: 0; padding: 0; box-sizing: border-box; }
  html, body {
    width: 1200px;
    height: 960px;
    overflow: hidden;
  }
  body {
    position: relative;
    background: var(--backdrop);
    font-family: "Roboto", Arial, sans-serif;
  }
  .card {
    position: absolute;
    width: 600px;
    height: 343px;
    box-shadow: 0 3px 8px var(--shadow);
  }
  /* Front side */
  .card-front {
    left: 314px;
    top: 113px;
    background: var(--card-white);
  }
  .name-band {
    position: absolute;
    left: 0;
    top: 45px;
    width: 286px;
    height: 55px;
    background: var(--teal);
    color: var(--card-white);
    padding: 5px 0 0 41px;
  }
  .person-name {
    font-weight: 700;
    font-size: 21px;
    letter-spacing: 0.3px;
    line-height: 26px;
  }
  .person-title {
    font-weight: 500;
    font-size: 14.5px;
    line-height: 18px;
  }
  .brand-front {
    position: absolute;
    right: 56px;
    top: 52px;
    display: flex;
    align-items: center;
    gap: 10px;
    color: var(--teal);
    font-weight: 500;
    font-size: 19px;
    line-height: 22px;
    letter-spacing: 1px;
  }
  .brand-square {
    width: 40px;
    height: 40px;
    background: var(--teal);
    flex: none;
  }
  .address {
    position: absolute;
    left: 41px;
    top: 159px;
    font-size: 14px;
    line-height: 18px;
    color: var(--text-grey);
    font-style: normal;
  }
  .contact-list {
    position: absolute;
    left: 41px;
    top: 224px;
    list-style: none;
    font-size: 14px;
    color: var(--text-grey);
  }
  .contact-item {
    display: flex;
    align-items: center;
    height: 19.3px;
  }
  .contact-icon {
    width: 13px;
    height: 13px;
    margin-right: 10px;
    fill: var(--teal);
    flex: none;
  }
  /* Back side */
  .card-back {
    left: 312px;
    top: 472px;
    background: var(--teal);
  }
  .brand-back {
    position: absolute;
    right: 22px;
    top: 240px;
    text-align: right;
    color: var(--card-white);
    font-weight: 500;
    font-size: 25px;
    line-height: 27px;
    letter-spacing: 1.2px;
  }
  .tagline {
    position: absolute;
    right: 18px;
    top: 309px;
    color: var(--card-white);
    font-size: 14.5px;
    letter-spacing: 0.2px;
  }
</style>
</head>
<body>

<section class="card card-front" aria-label="Business card front">
  <div class="name-band">
    <p class="person-name">DANIEL OKAFOR</p>
    <p class="person-title">CEO/FOUNDER</p>
  </div>

  <div class="brand-front">
    <span class="brand-square" aria-hidden="true"></span>
    <span class="brand-name">HOLVASTER<br>BUILDING INC.</span>
  </div>

  <address class="address">
    18 North Tamlin Glen Road<br>
    Unit 57, Marbrook Vale, ON<br>
    K7T 2R9
  </address>

  <ul class="contact-list">
    <li class="contact-item">
      <svg class="contact-icon" viewBox="0 0 16 16" aria-hidden="true"><path d="M3.6 1.2l2.3 2.8-1.3 1.8c.9 2 2.5 3.6 4.5 4.5l1.8-1.3 2.8 2.3-1.4 2.9C6.8 14 2 9.2 1.8 3.1z"/></svg>
      905-218-5937
    </li>
    <li class="contact-item">
      <svg class="contact-icon" viewBox="0 0 16 16" aria-hidden="true"><path d="M4 0h8v16H4zM5.5 2v10h5V2zM7.3 13.3h1.4v1.4H7.3z" fill-rule="evenodd"/></svg>
      905-218-6041
    </li>
    <li class="contact-item">
      <svg class="contact-icon" viewBox="0 0 16 16" aria-hidden="true"><path d="M1 3h14v1.5L8 9 1 4.5zM1 6.3l7 4.5 7-4.5V13H1z"/></svg>
      info@holvaster-example.com
    </li>
    <li class="contact-item">
      <svg class="contact-icon" viewBox="0 0 16 16" aria-hidden="true"><circle cx="8" cy="8" r="7"/><path d="M1.5 8h13M8 1c-2.5 3-2.5 11 0 14M8 1c2.5 3 2.5 11 0 14" stroke="#fff" stroke-width="1" fill="none"/></svg>
      www.holvaster-example.com
    </li>
  </ul>
</section>

<section class="card card-back" aria-label="Business card back">
  <p class="brand-back">HOLVASTER<br>BUILDING INC.</p>
  <p class="tagline">Professional. Quality. Service.</p>
</section>

</body>
</html>
```